Meridale Cleaning Services

In need of a business card design suited for a growing cleaning company.

We offer our cleaning and maintenance services to a wide range of clients including but not limited to the following: constuction industry, hospitality, commercial, industrial and domestic

I want the card to be very noticable, i would like people to say 'hey, great card!' when i hand them my card.double sided would be nice

we want our business to come across as exceedingly professional and innovative (different).

a contemporary design is what we have in mind
we want to present an image of a quality business with a high standard of excellence in consistent service.

i just really need a card that persuades top end quality,
our business is very certified and also strives towards environmentaly friendly alternatives
Updates

hey sorry, i have uploaded my company logo design and name
cheers.

hey guys i have added my company logo/name file on my brief page. many thanks

sorry guys a typo in the brief..
address is Tolley Rd. not Tolly Rd
thanks

Industry/Entity Type

Industrial

Requirements
Must have
• company name: meridale cleaning services
operations manager: Colm Varetti
Tel: (02)9373 6204
Fax: (02)8645 7712
Mob: 0438571490

address: 47 Tolly RD Pymble NSW 2073
Postal Adress: PO Box 5832 North Ryde NSW 2113
email: meridaleclean@wexanet.com.au
website: meridalecleaningservices.com.au

```html
<!DOCTYPE html>
<html lang="en">
<head>
<meta charset="utf-8">
<title>Meridale Cleaning Services – Business Cards</title>
<link rel="stylesheet" href="https://fonts.googleapis.com/css2?family=Roboto+Condensed:wght@400;700&display=swap">
<style>
  :root {
    --backdrop: #666666;
    --card: #ffffff;
    --brand-blue: #1570c2;
    --ink: #1a1a1a;
    --mark: #2a8fd6;
  }
  html, body {
    margin: 0;
    padding: 0;
    width: 1099px;
    height: 1200px;
    overflow: hidden;
    background: var(--backdrop);
    font-family: "Roboto Condensed", "Arial Narrow", sans-serif;
  }
  .canvas {
    position: relative;
    width: 1099px;
    height: 1200px;
  }
  .card {
    position: absolute;
    left: 100px;
    width: 899px;
    background: var(--card);
    border-radius: 22px;
  }
  .card--front { top: 72px; height: 500px; }
  .card--back  { top: 638px; height: 496px; }

  .brand {
    display: flex;
    align-items: center;
    gap: 22px;
  }
  .brand__dot {
    flex: none;
    border-radius: 50%;
    background: var(--mark);
  }
  .brand__name {
    color: var(--brand-blue);
    font-weight: 700;
    white-space: nowrap;
    line-height: 1;
  }

  /* Front */
  .card--front .brand {
    position: absolute;
    top: 115px;
    left: 0;
    right: 0;
    justify-content: center;
  }
  .card--front .brand__dot { width: 130px; height: 130px; }
  .card--front .brand__name { font-size: 42px; }
  .card--front .person {
    position: absolute;
    top: 222px;
    left: 0;
    right: 0;
    text-align: center;
    color: var(--brand-blue);
  }
  .card--front .person__name { font-size: 32px; line-height: 40px; }
  .card--front .person__role { font-size: 29px; line-height: 40px; }
  .card--front .contact {
    position: absolute;
    top: 362px;
    left: 0;
    right: 0;
    text-align: center;
    color: var(--ink);
    font-size: 23px;
    line-height: 35px;
  }

  /* Back */
  .card--back .person {
    position: absolute;
    top: 47px;
    left: 216px;
    color: var(--ink);
    font-size: 25px;
    line-height: 31px;
  }
  .card--back .brand {
    position: absolute;
    top: 172px;
    left: 63px;
  }
  .card--back .brand__dot { width: 128px; height: 128px; }
  .card--back .brand__name { font-size: 40px; }
  .card--back .contact {
    position: absolute;
    top: 356px;
    left: 216px;
    color: var(--ink);
    font-size: 20px;
    line-height: 35px;
  }
  .contact p, .person p { margin: 0; }
</style>
</head>
<body>
<main class="canvas">

  <section class="card card--front" aria-label="Business card front">
    <div class="brand">
      <span class="brand__dot" aria-hidden="true"></span>
      <span class="brand__name">Meridale Cleaning Services</span>
    </div>
    <div class="person">
      <p class="person__name">Colm Varetti</p>
      <p class="person__role">Operations Manager</p>
    </div>
    <div class="contact">
      <p>47 Tolley RD Pymble NSW 2073 | PO Box 5832 North Ryde NSW 2113</p>
      <p>T (02)9373 6204 | F (02)8645 7712 | M 0438571490</p>
      <p>meridaleclean@wexanet.com.au | www.meridalecleaningservices.com.au</p>
    </div>
  </section>

  <section class="card card--back" aria-label="Business card back">
    <div class="person">
      <p class="person__name">Colm Varetti</p>
      <p class="person__role">Operations Manager</p>
    </div>
    <div class="brand">
      <span class="brand__dot" aria-hidden="true"></span>
      <span class="brand__name">Meridale Cleaning Services</span>
    </div>
    <div class="contact">
      <p>47 Tolley RD Pymble NSW 2073 | PO Box 5832 North Ryde NSW 2113</p>
      <p>T (02)9373 6204 | F (02)8645 7712 | M 0438571490</p>
      <p>meridaleclean@wexanet.com.au | www.meridalecleaningservices.com.au</p>
    </div>
  </section>

</main>
</body>
</html>
```